Roofing Company Sales Rep Business Card

Business card for sales rep to canvass and hand out to property owners/managers for free roof inspections and roof replacements.

```html
<!DOCTYPE html>
<html lang="en">
<head>
<meta charset="utf-8">
<title>Summit Crest Roofing – Business Card</title>
<link href="https://fonts.googleapis.com/css2?family=Poppins:wght@400;500;700&display=swap" rel="stylesheet">
<style>
  :root {
    --stage: #262626;
    --card: #0c0c0c;
    --card-edge: #1c1c1c;
    --white: #f4f4f4;
    --silver: #c9c9c9;
    --red: #e3141c;
    --rule: #4a4a4a;
  }
  * { margin: 0; padding: 0; box-sizing: border-box; }
  html, body {
    width: 1200px; height: 900px; overflow: hidden;
    background: var(--stage);
    font-family: "Poppins", sans-serif;
  }
  .stage {
    width: 1200px; height: 900px;
    display: flex; flex-direction: column;
    align-items: center; justify-content: center; gap: 50px;
  }
  .card {
    width: 630px; height: 360px;
    background: var(--card);
    border-radius: 26px;
    border: 1px solid var(--card-edge);
    position: relative;
    color: var(--white);
  }
  /* front */
  .card--front { display: flex; align-items: center; }
  .brand {
    width: 300px; display: flex; align-items: center; justify-content: center; gap: 10px;
  }
  .brand__mark { width: 14px; height: 14px; background: var(--red); flex: none; }
  .brand__name {
    font-weight: 700; font-size: 24px; line-height: 1.1; color: var(--white);
    letter-spacing: 0.5px;
  }
  .divider { width: 1px; height: 190px; background: var(--rule); }
  .contact { padding-left: 34px; }
  .contact__name { color: var(--red); font-size: 22px; font-weight: 500; line-height: 1.1; letter-spacing: 0.5px; }
  .contact__role { font-size: 16px; margin-bottom: 14px; }
  .contact__list { list-style: none; font-size: 16px; line-height: 1.6; }
  .contact__list li { display: flex; align-items: center; gap: 9px; }
  .contact__list svg { width: 15px; height: 15px; fill: var(--red); flex: none; }
  .accent { color: var(--red); }
  .contact__address { font-size: 16px; line-height: 1.35; margin-top: 10px; }
  /* back */
  .card--back {
    display: flex; flex-direction: column; align-items: center; justify-content: center; gap: 38px;
  }
  .card--back .brand { width: auto; }
  .card--back .brand__name { font-size: 36px; color: var(--silver); }
  .card--back .brand__mark { width: 20px; height: 20px; background: var(--silver); }
  .tagline { color: var(--red); font-size: 17px; letter-spacing: 0.4px; text-transform: uppercase; }
</style>
</head>
<body>
<main class="stage">
  <section class="card card--front">
    <div class="brand">
      <span class="brand__mark"></span>
      <span class="brand__name">SUMMIT CREST<br>ROOFING</span>
    </div>
    <div class="divider"></div>
    <div class="contact">
      <p class="contact__name">DANIEL HARPER</p>
      <p class="contact__role">Managing Director</p>
      <ul class="contact__list">
        <li><svg viewBox="0 0 24 24"><path d="M6.6 10.8a15.2 15.2 0 0 0 6.6 6.6l2.2-2.2a1 1 0 0 1 1-.25 11.4 11.4 0 0 0 3.6.57 1 1 0 0 1 1 1V20a1 1 0 0 1-1 1A17 17 0 0 1 3 4a1 1 0 0 1 1-1h3.5a1 1 0 0 1 1 1c0 1.25.2 2.45.57 3.57a1 1 0 0 1-.25 1z"/></svg><span>044-555 019 321</span></li>
        <li><svg viewBox="0 0 24 24"><path d="M2 5h20v14H2zm2 2v.5l8 6 8-6V7z"/></svg><span>info@summitcrest.com</span></li>
        <li><svg viewBox="0 0 24 24"><path d="M12 2a10 10 0 1 0 0 20 10 10 0 0 0 0-20zm6.9 6h-3a15.6 15.6 0 0 0-1.3-4A8 8 0 0 1 18.9 8zM12 4c.8 1.2 1.5 2.5 1.9 4h-3.8c.4-1.5 1.1-2.8 1.9-4zM4.3 14a8 8 0 0 1 0-4h3.4a16 16 0 0 0 0 4zm.8 2h3a15.6 15.6 0 0 0 1.3 4A8 8 0 0 1 5.1 16zm3-8h-3a8 8 0 0 1 4.3-4 15.6 15.6 0 0 0-1.3 4zM12 20c-.8-1.2-1.5-2.5-1.9-4h3.8c-.4 1.5-1.1 2.8-1.9 4zm2.3-6H9.7a14.6 14.6 0 0 1 0-4h4.6a14.6 14.6 0 0 1 0 4zm.3 6a15.6 15.6 0 0 0 1.3-4h3a8 8 0 0 1-4.3 4zm1.7-6a16 16 0 0 0 0-4h3.4a8 8 0 0 1 0 4z"/></svg><span>www.<span class="accent">summitcrestroofing</span>.com</span></li>
      </ul>
      <p class="contact__address">18 Ridgeway Lane, Suite 4<br>62704, Springfield</p>
    </div>
  </section>

  <section class="card card--back">
    <div class="brand">
      <span class="brand__mark"></span>
      <span class="brand__name">SUMMIT CREST ROOFING</span>
    </div>
    <p class="tagline">Free roof inspections and roof replacements</p>
  </section>
</main>
</body>
</html>
```